Need a book cover design for a Lumora Book on Herbal Remedies

I need a book cover for my new ebook, here are the details:
Title: Meadow Cures
Sub-Heading: Buried Ancient Garden Tonics
Reclaiming the Wisdom of Roots for Everyday Wellness and Strength
Author: Nora Belcourt

```html
<!DOCTYPE html>
<html lang="en">
<head>
<meta charset="utf-8">
<title>Meadow Cures — Nora Belcourt</title>
<link href="https://fonts.googleapis.com/css2?family=Playfair+Display:wght@700;800&family=Montserrat:wght@500;600&display=swap" rel="stylesheet">
<style>
  :root {
    --page: #ffffff;
    --parchment-light: #f4ecc4;
    --parchment: #e9dca6;
    --parchment-deep: #d9c483;
    --leaf-dark: #3f6a1e;
    --leaf: #6f9a33;
    --leaf-light: #9fbf52;
    --olive: #5d7424;
    --lime: #cfe36b;
    --amber: #8a4b1c;
  }
  * { box-sizing: border-box; margin: 0; padding: 0; }
  html, body { width: 1200px; height: 886px; overflow: hidden; background: var(--page); }

  .cover {
    position: absolute; left: 343px; top: 33px;
    width: 514px; height: 820px; overflow: hidden;
    box-shadow: 0 14px 22px -12px rgba(0,0,0,.35);
  }
  .cover-art {
    position: absolute; inset: 0;
    background:
      radial-gradient(ellipse 60% 22% at 60% 0%, var(--leaf) 0%, rgba(111,154,51,.55) 45%, transparent 80%),
      radial-gradient(ellipse 18% 14% at 0% 6%, var(--amber) 0%, transparent 90%),
      radial-gradient(ellipse 18% 12% at 100% 9%, #a0783a 0%, transparent 90%),
      radial-gradient(ellipse 14% 22% at 0% 30%, var(--leaf) 0%, transparent 90%),
      radial-gradient(ellipse 8% 30% at 100% 45%, #7b6f9a 0%, transparent 85%),
      radial-gradient(ellipse 70% 13% at 50% 100%, var(--leaf-dark) 0%, rgba(111,154,51,.6) 50%, transparent 90%),
      radial-gradient(ellipse 14% 14% at 100% 85%, var(--leaf-light) 0%, transparent 90%),
      radial-gradient(ellipse 80% 60% at 50% 50%, var(--parchment-light) 0%, var(--parchment) 60%, var(--parchment-deep) 100%);
  }

  .cover-text {
    position: absolute; inset: 0;
    display: flex; flex-direction: column; align-items: center;
    color: var(--olive);
  }
  .title {
    margin-top: 256px;
    font-family: "Playfair Display", serif; font-weight: 800;
    font-size: 72px; line-height: 0.92; text-align: center;
    text-transform: uppercase; letter-spacing: -1px;
  }
  .subtitle-band {
    margin-top: 12px;
    width: 352px; height: 40px;
    background: var(--olive); color: var(--lime);
    font-family: "Montserrat", sans-serif; font-weight: 600;
    font-size: 15.5px; text-transform: uppercase;
    display: flex; align-items: center; justify-content: center;
  }
  .tagline {
    margin-top: 40px;
    font-family: "Montserrat", sans-serif; font-weight: 600;
    font-size: 20px; line-height: 30px; letter-spacing: 1px;
    text-align: center; text-transform: uppercase;
  }
  .sprig {
    margin-top: 48px;
    width: 120px; height: 22px; border-radius: 50%;
    background: radial-gradient(ellipse at center, rgba(93,116,36,.7) 0%, rgba(93,116,36,.25) 60%, transparent 100%);
  }
  .author-row {
    margin-top: 18px;
    display: flex; align-items: center; gap: 8px;
  }
  .author-rule { width: 118px; height: 1.5px; background: var(--olive); }
  .author {
    font-family: "Playfair Display", serif; font-weight: 700;
    font-size: 22px; text-transform: uppercase; letter-spacing: -0.5px;
  }
</style>
</head>
<body>
  <div class="cover">
    <div class="cover-art" role="img" aria-label="Photograph of fresh herbs, ferns, flowers and jars of capsules framing an aged parchment background"></div>
    <div class="cover-text">
      <h1 class="title">Meadow<br>Cures</h1>
      <p class="subtitle-band">Buried Ancient Garden Tonics</p>
      <p class="tagline">Reclaiming the Wisdom<br>of Roots for<br>Everyday Wellness<br>and Strength</p>
      <div class="sprig" role="img" aria-label="Small rosemary sprig illustration"></div>
      <div class="author-row">
        <span class="author-rule"></span>
        <p class="author">Nora Belcourt</p>
        <span class="author-rule"></span>
      </div>
    </div>
  </div>
</body>
</html>
```